Fresh, modern, fun business card for pediatric dental practice

Need a business card for fresh, modern, fun pediatric dental practice

Clean look that matches our website's font and colors

We prefer the look of curved corners on business cards

Target Market(s)

parents (mothers) of young children, professionals, mid-high class

Industry/Entity Type

Dental

Contact Information for Business Card

Maplebrook Pediatric Dentistry
482 Orchard Vale Road
Suite 517
Fernwick, PA 17091
555.419.3067
www.maplebrookkidsdental.example

Mara Tevlin, DMD
Colette Varnum, DMD
(we are working on our email address, but we would like that on the card as well)

Font styles to use
Sans Serif

Requirements
Must have
• All info; we would also like to make cards for individual staff members
• colors from our website and color palatte, attatched
• use same font and design as website for branding
Nice to have
• clean, simple card that has a pop of color
• we would like to see a few designs with our tag line "where smiles get brighter"
• we are not sure if we want to have it on there or not
• we would like to see a few designs incorporating the ribbon graphic on our website where the word WELCOME is

```html
<!DOCTYPE html>
<html lang="en">
<head>
<meta charset="utf-8">
<title>Maplebrook Pediatric Dentistry – Business Card</title>
<link rel="stylesheet" href="https://fonts.googleapis.com/css2?family=Questrial&family=Varela+Round&display=swap">
<style>
  :root {
    --plum: #4e2351;
    --sun: #f7b21c;
    --magenta: #d9329a;
    --ink: #3a3a3a;
    --paper: #ffffff;
    --backdrop: #ece8e4;
  }
  * { margin: 0; padding: 0; box-sizing: border-box; }
  html, body { width: 1200px; height: 889px; overflow: hidden; }
  body {
    background: var(--backdrop);
    font-family: "Questrial", sans-serif;
    color: var(--ink);
    position: relative;
  }
  .card {
    position: absolute;
    left: 250px;
    width: 700px;
    height: 400px;
    border-radius: 26px;
    box-shadow: 0 6px 18px rgba(0,0,0,.12);
    overflow: hidden;
  }
  .card-front { top: 24px; background: var(--paper); }
  .card-back { top: 465px; background: var(--plum); }

  .wordmark {
    position: absolute;
    font-family: "Varela Round", sans-serif;
    color: var(--sun);
    line-height: 1.05;
    display: flex;
    align-items: center;
    gap: 14px;
  }
  .wordmark-dot {
    border-radius: 50%;
    background: var(--sun);
    flex: none;
  }
  .card-front .wordmark { left: 52px; top: 44px; font-size: 34px; }
  .card-front .wordmark-dot { width: 22px; height: 22px; }

  .address {
    position: absolute;
    left: 52px; top: 150px;
    font-size: 17px;
    line-height: 1.5;
  }

  .person {
    position: absolute;
    left: 330px; top: 218px;
  }
  .person-name {
    font-family: "Varela Round", sans-serif;
    font-weight: 400;
    color: var(--magenta);
    font-size: 27px;
    padding-bottom: 10px;
    border-bottom: 2px solid var(--sun);
    display: inline-block;
    padding-right: 20px;
  }
  .contacts { list-style: none; margin-top: 14px; font-size: 16px; line-height: 1.75; }
  .contacts li { display: flex; align-items: center; gap: 10px; }
  .contacts svg { width: 14px; height: 14px; flex: none; }
  .web-domain { color: var(--magenta); }

  .card-back .wordmark {
    left: 0; right: 0; top: 130px;
    justify-content: center;
    font-size: 46px;
    text-align: left;
  }
  .card-back .wordmark-dot { width: 30px; height: 30px; }
  .card-back .site {
    position: absolute;
    left: 0; right: 0; top: 300px;
    text-align: center;
    color: var(--sun);
    font-size: 18px;
    letter-spacing: .3px;
  }
</style>
</head>
<body>

<section class="card card-front" aria-label="Business card front">
  <div class="wordmark">
    <span class="wordmark-dot"></span>
    <span>Maplebrook<br>Pediatric Dentistry</span>
  </div>
  <p class="address">
    Maplebrook Pediatric Dentistry<br>
    482 Orchard Vale Road<br>
    Suite 517, Fernwick, PA 17091
  </p>
  <div class="person">
    <h1 class="person-name">Mara Tevlin, DMD</h1>
    <ul class="contacts">
      <li>
        <svg viewBox="0 0 16 16" aria-hidden="true"><path d="M4 1.5l2.3 3-1.4 1.6c.8 1.9 2.3 3.4 4.2 4.2l1.6-1.4 3 2.3-1.3 2.6C7.3 13.6 2.4 8.7 1.5 3z" fill="none" stroke="#d9329a" stroke-width="1.5" stroke-linejoin="round"/></svg>
        555.419.3067
      </li>
      <li>
        <svg viewBox="0 0 16 16" aria-hidden="true"><rect x="1.5" y="3.5" width="13" height="9" rx="1" fill="none" stroke="#d9329a" stroke-width="1.5"/><path d="M1.5 4l6.5 5 6.5-5" fill="none" stroke="#d9329a" stroke-width="1.5"/></svg>
        info@maplebrookkidsdental.example
      </li>
      <li>
        <svg viewBox="0 0 16 16" aria-hidden="true"><circle cx="8" cy="8" r="6.5" fill="none" stroke="#d9329a" stroke-width="1.5"/><path d="M1.5 8h13M8 1.5c-3 3.5-3 9.5 0 13M8 1.5c3 3.5 3 9.5 0 13" fill="none" stroke="#d9329a" stroke-width="1.2"/></svg>
        <span>www.<span class="web-domain">maplebrookkidsdental</span>.example</span>
      </li>
    </ul>
  </div>
</section>

<section class="card card-back" aria-label="Business card back">
  <div class="wordmark">
    <span class="wordmark-dot"></span>
    <span>Maplebrook<br>Pediatric Dentistry</span>
  </div>
  <p class="site">www.maplebrookkidsdental.example</p>
</section>

</body>
</html>
```